Scientific and medical consulting company needs "not a plain" business card.

I need a business card that looks different, or made differently, or functions as something. I am seeking to give it out at a medical device conference to get business and initial contacts. The final design should communicate medical competence, scientific know how, and creativity.

It needs to use my existing logo (created on Loomra Works!).
Each side should be something different., have different style.

```html
<!DOCTYPE html>
<html lang="en">
<head>
<meta charset="utf-8">
<title>Velmora Labs – Business Card</title>
<link href="https://fonts.googleapis.com/css2?family=Quicksand:wght@500;600;700&display=swap" rel="stylesheet">
<style>
  :root {
    --backdrop: #c9c9c9;
    --brand-blue: #1f5da3;
    --deep-blue: #1c4f93;
    --brand-green: #5cbf45;
    --light-green: #8fd35a;
    --teal: #3fa9d6;
    --paper: #f7f7f7;
    --white: #ffffff;
    --text-blue: #1f5da3;
    --muted-green: #4aa63a;
  }
  * { box-sizing: border-box; margin: 0; padding: 0; }
  html, body { width: 1200px; height: 454px; overflow: hidden; }
  body {
    background: var(--backdrop);
    font-family: "Quicksand", "Trebuchet MS", sans-serif;
    position: relative;
  }
  .card {
    position: absolute;
    top: 59px;
    width: 520px;
    height: 336px;
    overflow: hidden;
    box-shadow: 0 6px 16px rgba(0,0,0,0.18);
  }

  /* Reverse side */
  .card-reverse {
    left: 60px;
    background: linear-gradient(125deg, var(--deep-blue) 0%, var(--brand-blue) 40%, var(--brand-green) 62%, var(--light-green) 100%);
  }
  .reverse-disc {
    position: absolute;
    left: 110px;
    top: 18px;
    width: 300px;
    height: 300px;
    border-radius: 50%;
    background: radial-gradient(circle at 40% 60%, var(--teal) 0%, #2a7fc0 55%, rgba(92,191,69,0.85) 100%);
    opacity: 0.9;
  }
  .reverse-name {
    position: absolute;
    left: 300px;
    top: 196px;
    color: var(--white);
    font-weight: 600;
    font-size: 26px;
    letter-spacing: -0.3px;
    white-space: nowrap;
  }
  .reverse-tagline {
    position: absolute;
    left: 302px;
    top: 230px;
    color: var(--white);
    font-weight: 500;
    font-size: 10.5px;
    white-space: nowrap;
    border-top: 1px solid rgba(255,255,255,0.8);
    padding-top: 2px;
  }

  /* Contact side */
  .card-contact {
    left: 620px;
    background: var(--paper);
  }
  .contact-panel {
    position: absolute;
    left: 0; top: 0;
    width: 100%; height: 100%;
  }
  .holder-name {
    position: absolute;
    left: 34px; top: 26px;
    color: var(--white);
    font-weight: 600;
    font-size: 21px;
    white-space: nowrap;
  }
  .holder-role {
    position: absolute;
    left: 34px; top: 62px;
    color: var(--white);
    font-weight: 600;
    font-size: 12.5px;
  }
  .contact-list {
    position: absolute;
    left: 26px; top: 100px;
    list-style: none;
  }
  .contact-list li {
    display: flex;
    align-items: center;
    gap: 8px;
    color: var(--white);
    font-weight: 600;
    font-size: 12.5px;
    height: 21px;
    white-space: nowrap;
  }
  .contact-list svg { width: 17px; height: 14px; flex: none; }
  .brand-disc {
    position: absolute;
    left: 352px; top: 50px;
    width: 104px; height: 104px;
    border-radius: 50%;
    background: linear-gradient(160deg, var(--brand-blue) 0%, var(--teal) 55%, var(--brand-green) 100%);
  }
  .brand-name {
    position: absolute;
    left: 296px; top: 168px;
    width: 214px;
    text-align: center;
    color: var(--text-blue);
    font-weight: 600;
    font-size: 27px;
    letter-spacing: -0.4px;
    white-space: nowrap;
  }
  .brand-tagline {
    position: absolute;
    left: 294px; top: 204px;
    width: 218px;
    text-align: center;
    color: var(--muted-green);
    font-weight: 600;
    font-size: 10px;
    white-space: nowrap;
    border-top: 1.5px solid var(--brand-green);
    padding-top: 2px;
  }
  .brand-address {
    position: absolute;
    left: 296px; top: 248px;
    width: 214px;
    text-align: center;
    color: var(--text-blue);
    font-weight: 700;
    font-size: 11.5px;
    white-space: nowrap;
  }
</style>
</head>
<body>

<section class="card card-reverse" aria-label="Card reverse">
  <div class="reverse-disc"></div>
  <p class="reverse-name">Velmora Labs</p>
  <p class="reverse-tagline">uniting research and clinical practice</p>
</section>

<section class="card card-contact" aria-label="Card contact side">
  <svg class="contact-panel" viewBox="0 0 520 336" aria-hidden="true">
    <defs>
      <clipPath id="panel-clip">
        <path d="M0 0 H228 L212 336 H0 Z"/>
      </clipPath>
    </defs>
    <path d="M220 0 H246 L230 336 H204 Z" fill="var(--light-green)"/>
    <path d="M0 0 H228 L212 336 H0 Z" fill="var(--brand-blue)"/>
    <g clip-path="url(#panel-clip)">
      <circle cx="150" cy="300" r="100" fill="var(--light-green)"/>
    </g>
  </svg>

  <h1 class="holder-name">Daniel Hartley</h1>
  <p class="holder-role">Managing Director</p>

  <ul class="contact-list">
    <li>
      <svg viewBox="0 0 17 14"><rect width="17" height="14" fill="var(--light-green)"/><path d="M2 3 H15 V11 H2 Z M2 3 L8.5 8 L15 3" fill="none" stroke="#fff" stroke-width="1.3"/></svg>
      daniel@velmoralabs.com
    </li>
    <li>
      <svg viewBox="0 0 17 14"><rect width="17" height="14" fill="var(--light-green)"/><circle cx="8.5" cy="7" r="5" fill="none" stroke="#fff" stroke-width="1.2"/><path d="M3.5 7 H13.5 M8.5 2 C6 5 6 9 8.5 12 M8.5 2 C11 5 11 9 8.5 12" fill="none" stroke="#fff" stroke-width="1"/></svg>
      www.velmoralabs.com
    </li>
    <li>
      <svg viewBox="0 0 17 14"><rect width="17" height="14" fill="var(--light-green)"/><path d="M3 5 C3 3 14 3 14 5 L12 6 L11 5 H6 L5 6 Z M5 7 H12 L13 12 H4 Z" fill="#fff"/></svg>
      01632960418
    </li>
    <li>
      <svg viewBox="0 0 17 14"><rect width="17" height="14" fill="var(--light-green)"/><rect x="6" y="1.5" width="5" height="11" rx="1" fill="none" stroke="#fff" stroke-width="1.3"/><circle cx="8.5" cy="10.5" r="0.8" fill="#fff"/></svg>
      07700900234
    </li>
  </ul>

  <div class="brand-disc"></div>
  <p class="brand-name">Velmora Labs</p>
  <p class="brand-tagline">uniting research and clinical practice</p>
  <p class="brand-address">27 Larkmoor Lane Brindlefield</p>
</section>

</body>
</html>
```